Stonebrook 720 Real Estate Investment Company

We need a business card designed for a real estate investment company named Stonebrook 720. We want to use red#f04a50, orange #f37122 and yellow #fbee3e as the color scheme. The logo colors will need to be modified from the current blue palette. I've attach VitaPathway logo example that captures the color scheme we're going for for Stonebrook 720. Looking for clean Sans Serif fonts.
Contact Information for Business Card
Daniel Furlow
Managing Partner
48317 Whitfield Lane, Suite 510
Tampa, FL 33718
813-555-4870 Mobile
dfurlow@stonebrook720.example
www.stonebrook720.example
Requirements
Must have
- Looking for creative responses.
Nice to have
- Must hit color palette... orange, red, yellow

```html
<!DOCTYPE html>
<html lang="en">
<head>
<meta charset="utf-8">
<title>Stonebrook 720 – Business Card</title>
<link rel="stylesheet" href="https://fonts.googleapis.com/css2?family=Roboto+Condensed:wght@400;700;800&display=swap">
<style>
  :root {
    --backdrop: #e7e4df;
    --card-white: #f4f4f4;
    --ink: #151515;
    --band-black: #0c0c0c;
    --brand-red: #f04a50;
    --brand-orange: #f37122;
    --brand-yellow: #fbee3e;
    --text-light: #ffffff;
  }
  * { box-sizing: border-box; margin: 0; padding: 0; }
  html, body {
    width: 1200px; height: 780px; overflow: hidden;
    background: var(--backdrop);
    font-family: "Roboto Condensed", Arial, sans-serif;
  }
  .stage {
    width: 1200px; height: 780px;
    display: flex; align-items: center; justify-content: center; gap: 60px;
  }
  .card {
    width: 525px; height: 300px; position: relative; overflow: hidden;
    box-shadow: 0 10px 24px rgba(0,0,0,.22);
  }
  /* Front */
  .card-front { background: var(--card-white); }
  .brand-area {
    height: 178px; display: flex; align-items: center; justify-content: center; gap: 14px;
  }
  .brand-name {
    font-weight: 800; font-size: 54px; letter-spacing: -0.5px; color: var(--ink);
    white-space: nowrap;
  }
  .brand-dot {
    width: 22px; height: 22px; border-radius: 50%; flex: none;
    background: var(--brand-orange);
  }
  .name-band {
    height: 32px; background: var(--band-black); color: var(--text-light);
    display: flex; align-items: center; padding-left: 142px; font-size: 16px;
  }
  .person-name { font-weight: 700; }
  .divider { margin: 0 10px; color: var(--brand-yellow); }
  .person-title { font-weight: 400; font-size: 14px; }
  .contact-band {
    height: 90px;
    background: linear-gradient(100deg, var(--brand-red) 0%, var(--brand-red) 55%, var(--brand-orange) 100%);
    color: var(--text-light);
    display: flex; justify-content: space-between; align-items: center;
    padding: 0 26px 0 30px; font-size: 14px; line-height: 1.45;
  }
  .contact-list { list-style: none; }
  .contact-list li { display: flex; align-items: center; gap: 8px; white-space: nowrap; }
  .contact-list svg { width: 12px; height: 12px; flex: none; }
  .contact-icon { fill: none; stroke: var(--brand-yellow); }
  .contact-icon-fill { fill: var(--brand-yellow); }
  .address { text-align: right; font-style: normal; white-space: nowrap; }
  /* Back */
  .card-back {
    background: var(--band-black);
    display: flex; align-items: center; justify-content: center; gap: 14px;
  }
  .card-back .brand-name { color: var(--text-light); font-size: 58px; }
  .card-back .brand-dot { background: var(--brand-yellow); }
</style>
</head>
<body>
<main class="stage">
  <section class="card card-front" aria-label="Business card front">
    <div class="brand-area">
      <span class="brand-name">Stonebrook 720</span>
      <span class="brand-dot" aria-hidden="true"></span>
    </div>
    <div class="name-band">
      <span class="person-name">Daniel Furlow</span>
      <span class="divider">|</span>
      <span class="person-title">Managing Partner</span>
    </div>
    <div class="contact-band">
      <ul class="contact-list">
        <li>
          <svg viewBox="0 0 12 12" aria-hidden="true"><rect class="contact-icon" x="3" y="0.5" width="6" height="11" rx="1" stroke-width="1.2"/><circle class="contact-icon-fill" cx="6" cy="9.5" r=".8"/></svg>
          813-555-4870
        </li>
        <li>
          <svg viewBox="0 0 12 12" aria-hidden="true"><rect class="contact-icon" x="0.5" y="2" width="11" height="8" stroke-width="1.2"/><path class="contact-icon" d="M0.5 2 L6 7 L11.5 2" stroke-width="1.2"/></svg>
          dfurlow@stonebrook720.example
        </li>
        <li>
          <svg viewBox="0 0 12 12" aria-hidden="true"><circle class="contact-icon" cx="6" cy="6" r="5.3" stroke-width="1.1"/><ellipse class="contact-icon" cx="6" cy="6" rx="2.3" ry="5.3" stroke-width="1"/><path class="contact-icon" d="M.7 6 H11.3" stroke-width="1"/></svg>
          www.stonebrook720.example
        </li>
      </ul>
      <address class="address">
        48317 Whitfield Lane<br>
        Suite 510<br>
        Tampa, FL 33718
      </address>
    </div>
  </section>

  <section class="card card-back" aria-label="Business card back">
    <span class="brand-name">Stonebrook 720</span>
    <span class="brand-dot" aria-hidden="true"></span>
  </section>
</main>
</body>
</html>
```